Velora Autohaus Nordic
Velora Autohaus Nordic - Automotive
Creative Brief
Modern
Velora Autohaus Nordic Oy
Автомобили и мототехника из США и Европы
info@veloraautohaus.example
www.veloraautohaus.example
The data that I would like to see: Velora Autohaus Nordic Oy Автомобили и мототехника из США и Европы (Cars and bikes from the U.S. and Europe) Контакты Phone: +7-918-647-20-83 (mobile phone) Skype: veloraautohaus Email: info@veloraautohaus.example www.veloraautohaus.example Генеральный директор (Director general) Белянский Артём Феликсович
On consideration of the developer. Will consider any options.

```html
<!DOCTYPE html>
<html lang="ru">
<head>
<meta charset="utf-8">
<title>Velora Autohaus Nordic — business card</title>
<link rel="stylesheet" href="https://fonts.googleapis.com/css2?family=Cormorant+SC:wght@500;600&family=PT+Serif:wght@400&display=swap">
<style>
  :root{
    --page:#e9eaec;
    --sky:#3fb2f2;
    --blue:#1c86d1;
    --deep:#0b3f6e;
    --night:#061a2c;
    --ink:#1d5e94;
    --muted:#6a7480;
    --paper:#ffffff;
    --paper-shade:#eef1f4;
  }
  *{box-sizing:border-box;margin:0;padding:0}
  html,body{width:1200px;height:1070px;overflow:hidden}
  body{background:var(--page);position:relative;font-family:"PT Serif",serif}
  .card{position:absolute;left:170px;width:860px;height:478px;border-radius:26px;overflow:hidden;
        box-shadow:0 10px 28px rgba(0,0,0,.18)}
  .card--front{top:36px;background:linear-gradient(180deg,var(--paper) 60%,var(--paper-shade))}
  .card--back{top:556px;background:radial-gradient(ellipse 90% 55% at 50% 0%,var(--sky) 0%,var(--blue) 30%,var(--deep) 62%,var(--night) 100%)}

  .front-band{height:196px;padding:38px 44px 0;
      background:linear-gradient(180deg,#67c6f7 0%,var(--sky) 22%,var(--blue) 55%,var(--deep) 85%,var(--night) 100%)}
  .brand-name{font-family:"Cormorant SC",serif;font-weight:600;color:#fff;font-size:58px;line-height:1;letter-spacing:.5px}
  .brand-tagline{margin-top:18px;color:#fff;font-size:22px;letter-spacing:.6px}

  .holder{text-align:center;margin-top:44px}
  .holder-company{color:var(--ink);font-size:26px}
  .holder-role{color:var(--muted);font-size:18px;margin-top:6px}

  .contacts{display:grid;grid-template-columns:270px 330px;column-gap:34px;row-gap:18px;
      justify-content:center;margin-top:40px;font-size:16px;color:#333}
  .contact{display:flex;align-items:center;gap:14px}
  .contact svg{width:22px;height:22px;flex:none}

  .back-lockup{position:absolute;left:0;right:0;top:120px;display:flex;align-items:center;justify-content:center;gap:30px}
  .back-lockup .dot{width:110px;height:110px;border-radius:50%;border:3px solid #fff;flex:none;
      box-shadow:0 0 30px rgba(120,200,255,.45)}
  .back-text{display:flex;flex-direction:column}
  .back-name{font-family:"Cormorant SC",serif;font-weight:600;color:#fff;font-size:62px;line-height:.95;letter-spacing:.5px}
  .back-tagline{margin-top:18px;color:#fff;font-size:19px;letter-spacing:.5px;white-space:nowrap}
</style>
</head>
<body>
  <section class="card card--front">
    <header class="front-band">
      <div class="brand-name">Velora Autohaus Nordic</div>
      <div class="brand-tagline">Автомобили и мототехника из США и Европы</div>
    </header>
    <div class="holder">
      <div class="holder-company">Velora Autohaus Nordic Oy</div>
      <div class="holder-role">Генеральный директор</div>
    </div>
    <div class="contacts">
      <div class="contact">
        <svg viewBox="0 0 24 24"><path d="M6.5 3l3 3.5-2 2.2a13 13 0 0 0 7.8 7.8l2.2-2 3.5 3-2.3 2.8C12 20 4 12 3.7 5.3z" fill="var(--blue)"/></svg>
        <span>+7-918-647-20-83</span>
      </div>
      <div class="contact">
        <svg viewBox="0 0 24 24"><rect x="2" y="5" width="20" height="14" rx="2" fill="var(--blue)"/><path d="M3 6.5l9 6.5 9-6.5" stroke="#fff" stroke-width="1.6" fill="none"/></svg>
        <span>info@veloraautohaus.example</span>
      </div>
      <div class="contact">
        <svg viewBox="0 0 24 24"><circle cx="12" cy="12" r="9" fill="var(--blue)"/><path d="M8 12.5l2.6 2.6L16 9.5" stroke="#fff" stroke-width="2" fill="none"/></svg>
        <span>veloraautohaus</span>
      </div>
      <div class="contact">
        <svg viewBox="0 0 24 24"><circle cx="12" cy="12" r="9" fill="none" stroke="var(--blue)" stroke-width="2"/><ellipse cx="12" cy="12" rx="4" ry="9" fill="none" stroke="var(--blue)" stroke-width="1.6"/><path d="M3 12h18" stroke="var(--blue)" stroke-width="1.6"/></svg>
        <span>www.veloraautohaus.example</span>
      </div>
    </div>
  </section>

  <section class="card card--back">
    <div class="back-lockup">
      <span class="dot"></span>
      <div class="back-text">
        <span class="back-name">Velora Autohaus<br>Nordic</span>
        <span class="back-tagline">Автомобили и мототехника из США и Европы</span>
      </div>
    </div>
  </section>
</body>
</html>
```